Stationery Design Project

Hi All,

We need you to design stationary for a new Business and Accounting Advisory Firm. We have already got the logo designed and it is attached. If you could also if possible, match the fonts in your design to that on the logo’s provided.

What we need:
- Business Card
- A4 Letter head
- A4 Folders
- PPT template (Title page and regular page)

And what ever else you want to throw in.

We are in the process of getting the web site designed, however below is a list of websites which we like which will give you an understanding of the style that we are going for.

- plinvo.example
- brightmarrow.example
- tallyquill.example
- framelotus.example

I look forward to your seeing your design.
Updates

Hi All,

I have just realised that I forgot that i need to include a Bonded Ledgermen image on the letter head, please find attaced as File 1. Could you please have this image in the bottom left header.

Regards,

Morwen

Industry/Entity Type

Business

Requirements
Must have
• Outputs:
- Documents ready to print
- Generic editable information
- Pdf copies of the documents
- Word version of letterhead

```html
<!DOCTYPE html>
<html lang="en">
<head>
<meta charset="utf-8">
<title>Tarrin Partners – Business Cards</title>
<link rel="stylesheet" href="https://fonts.googleapis.com/css2?family=EB+Garamond:wght@500&family=Tinos:wght@400;700&display=swap">
<style>
  :root {
    --backdrop: #8a8d90;
    --paper: #ffffff;
    --card-edge: #6f7275;
    --brand-blue: #3a5a9c;
    --brand-navy: #2f4f8f;
    --brand-sky: #3fb6d8;
    --band-blue: #2f83c2;
    --band-orange: #f7a21e;
    --accent-orange: #f59a1e;
    --ink: #1e1e1e;
    --rule: #8c8c8c;
    --icon: #3a6fb0;
  }
  * { box-sizing: border-box; margin: 0; padding: 0; }
  html, body { width: 1200px; height: 709px; overflow: hidden; background: var(--backdrop); }
  .sheet { position: relative; width: 1200px; height: 709px; }

  .card {
    position: absolute;
    width: 558px;
    height: 319px;
    background: var(--paper);
    border: 1px solid var(--card-edge);
    overflow: hidden;
  }
  .card--front { left: 323px; top: 20px; }
  .card--back-light { left: 23px; top: 356px; }
  .card--back-dark {
    left: 616px; top: 356px;
    border: none;
    background: radial-gradient(circle at 288px 165px, var(--brand-sky) 0%, #3a7fb8 30%, var(--brand-blue) 68%);
  }

  .lockup { position: absolute; display: flex; align-items: center; gap: 14px; }
  .lockup__dot { width: 58px; height: 58px; border-radius: 50%; background: var(--accent-orange); flex: none; }
  .lockup__name {
    font-family: "EB Garamond", Georgia, serif;
    font-weight: 500;
    font-size: 34px;
    color: var(--brand-blue);
    white-space: nowrap;
    letter-spacing: 0.2px;
  }
  .card--front .lockup { left: 0; right: 0; justify-content: center; top: 54px; }
  .card--back-light .lockup { left: 0; right: 0; justify-content: center; top: 112px; }
  .card--back-light .lockup__name { font-size: 38px; }
  .card--back-light .lockup__dot { width: 66px; height: 66px; }

  .identity {
    position: absolute; right: 300px; top: 166px;
    text-align: right;
    font-family: Tinos, "Times New Roman", serif;
    color: var(--ink);
  }
  .identity__name { font-size: 21px; font-weight: 700; color: var(--brand-blue); line-height: 24px; }
  .identity__role { font-size: 16px; line-height: 20px; margin-bottom: 6px; }
  .identity__address { font-size: 16px; line-height: 18px; font-style: normal; }

  .divider { position: absolute; left: 276px; top: 164px; width: 1px; height: 96px; background: var(--rule); }

  .contacts {
    position: absolute; left: 292px; top: 176px;
    list-style: none;
    font-family: Tinos, "Times New Roman", serif;
    font-size: 17px; color: var(--ink);
  }
  .contacts li { display: flex; align-items: center; gap: 6px; height: 27px; }
  .contacts svg { width: 13px; height: 13px; fill: var(--icon); flex: none; }

  .footer-band { position: absolute; left: 0; bottom: 0; width: 558px; height: 30px; }
  .footer-band__url {
    position: absolute; right: 22px; bottom: 6px;
    font-family: Tinos, "Times New Roman", serif;
    font-size: 16px; letter-spacing: 1.4px; color: var(--paper);
  }

  .web {
    position: absolute; left: 0; right: 0;
    text-align: center;
    font-family: Tinos, "Times New Roman", serif;
    font-size: 19px; letter-spacing: 1.6px;
  }
  .card--back-light .web { top: 240px; color: var(--ink); }
  .card--back-dark .web { top: 266px; color: var(--paper); }

  .card--back-dark .lockup { left: 0; right: 0; justify-content: center; top: 130px; }
  .card--back-dark .lockup__name { color: var(--paper); font-size: 50px; }
</style>
</head>
<body>
<main class="sheet">

  <section class="card card--front" aria-label="Business card front">
    <div class="lockup">
      <span class="lockup__dot"></span>
      <span class="lockup__name">Tarrin Partners</span>
    </div>

    <div class="identity">
      <p class="identity__name">Your Name</p>
      <p class="identity__role">Designation</p>
      <address class="identity__address">Street Name, City Name<br>State, City Zip Code</address>
    </div>

    <span class="divider"></span>

    <ul class="contacts">
      <li>
        <svg viewBox="0 0 16 16" aria-hidden="true"><path d="M8 0a8 8 0 1 0 0 16A8 8 0 0 0 8 0zm0 1.5a6.5 6.5 0 1 1 0 13 6.5 6.5 0 0 1 0-13zM5.2 4.2l1.6-.3.9 2.1-1 .8c.5 1.1 1.3 1.9 2.4 2.4l.8-1 2.1.9-.3 1.6c-3.5.2-6.7-3-6.5-6.5z"/></svg>
        0123-456-789
      </li>
      <li>
        <svg viewBox="0 0 16 16" aria-hidden="true"><path d="M3 7l1.6-4h6.8L13 7h1v5h-1.5v2H11v-2H5v2H3.5v-2H2V7h1zm2.2-2.6L4.3 7h7.4l-.9-2.6H5.2zM4.5 9a1 1 0 1 0 0 2 1 1 0 0 0 0-2zm7 0a1 1 0 1 0 0 2 1 1 0 0 0 0-2z"/></svg>
        0123-456-789
      </li>
      <li>
        <svg viewBox="0 0 16 16" aria-hidden="true"><path d="M1 6l7-4 7 4v8H1V6zm1.6.6L8 10l5.4-3.4L8 3.6 2.6 6.6z"/></svg>
        info@tarrinpartners.example
      </li>
    </ul>

    <div class="footer-band">
      <svg width="558" height="30" viewBox="0 0 558 30" aria-hidden="true">
        <defs>
          <linearGradient id="band-orange" x1="0" x2="1">
            <stop offset="0" stop-color="#f7b733"/>
            <stop offset="1" stop-color="#f48a12"/>
          </linearGradient>
          <linearGradient id="band-blue" x1="0" x2="1">
            <stop offset="0" stop-color="#3ba3d6"/>
            <stop offset="1" stop-color="#2a6fb4"/>
          </linearGradient>
        </defs>
        <polygon points="0,14 290,14 278,30 0,30" fill="url(#band-orange)"/>
        <polygon points="306,0 558,0 558,30 286,30" fill="url(#band-blue)"/>
      </svg>
      <span class="footer-band__url">www.tarrinpartners.example</span>
    </div>
  </section>

  <section class="card card--back-light" aria-label="Business card back, light">
    <div class="lockup">
      <span class="lockup__dot"></span>
      <span class="lockup__name">Tarrin Partners</span>
    </div>
    <p class="web">www.tarrinpartners.example</p>
  </section>

  <section class="card card--back-dark" aria-label="Business card back, blue">
    <div class="lockup">
      <span class="lockup__name">Tarrin Partners</span>
    </div>
    <p class="web">www.tarrinpartners.example</p>
  </section>

</main>
</body>
</html>
```